business card for trucking industry consulting firm

Our company, Velkor Services Inc. provides numerous services to the trucking industry as listed on our website: velkor.ca
The logo i want on the card is the black and red VELKOR
update: i would like the services we provide listed on the card (see velkor.ca)

```html
<!DOCTYPE html>
<html lang="en">
<head>
<meta charset="utf-8">
<title>Velkor Services Inc. – Business Card</title>
<link href="https://fonts.googleapis.com/css2?family=Lato:wght@400;700;900&display=swap" rel="stylesheet">
<style>
  :root {
    --stage: #3a3330;
    --card: #111111;
    --divider: #2c2c2c;
    --white: #f2f2f2;
    --grey: #c9c9c9;
    --silver: #b8b8b8;
    --muted: #8a8a8a;
    --red: #d42a2a;
  }
  * { box-sizing: border-box; margin: 0; padding: 0; }
  html, body { width: 1200px; height: 844px; overflow: hidden; }
  body {
    background: var(--stage);
    font-family: "Lato", Arial, sans-serif;
    position: relative;
  }
  .card {
    position: absolute;
    top: 272px;
    width: 525px;
    height: 300px;
    background: var(--card);
    border-radius: 3px;
    box-shadow: 0 10px 28px rgba(0,0,0,.45);
  }
  .card--front { left: 50px; }
  .card--back  { left: 625px; }

  .wordmark {
    position: absolute;
    text-align: center;
    font-weight: 900;
    color: var(--white);
    line-height: 1;
  }
  .wordmark__name { font-size: 48px; letter-spacing: 1px; display: block; }
  .wordmark__sub  { font-size: 19px; letter-spacing: 4px; display: block; margin-top: 8px; }

  .card--front .wordmark { left: 24px; top: 108px; width: 230px; }
  .card--back .wordmark { left: 0; right: 0; top: 80px; color: var(--silver); }
  .card--back .wordmark__name { font-size: 58px; }
  .card--back .wordmark__sub { font-size: 22px; }

  .divider {
    position: absolute;
    left: 268px; top: 0; bottom: 0;
    width: 1px;
    background: var(--divider);
  }
  .contact {
    position: absolute;
    left: 290px; top: 82px;
    color: var(--grey);
    font-size: 14px;
    line-height: 20px;
  }
  .contact__name { color: var(--red); font-weight: 700; font-size: 15px; letter-spacing: .5px; text-transform: uppercase; }
  .contact__title { margin-bottom: 2px; }
  .contact__row { display: flex; align-items: center; gap: 7px; }
  .contact__row svg { width: 10px; height: 10px; flex: none; }
  .contact__address { margin-top: 2px; }

  .services {
    position: absolute;
    left: 40px; right: 40px; bottom: 46px;
    display: flex;
    flex-wrap: wrap;
    justify-content: center;
    gap: 6px 0;
    list-style: none;
    color: var(--muted);
    font-size: 12px;
    letter-spacing: 1px;
    text-transform: uppercase;
  }
  .services li { padding: 0 10px; }
  .services li + li { border-left: 1px solid var(--red); }
  .services li:nth-child(4) { border-left: none; }
</style>
</head>
<body>
  <section class="card card--front" aria-label="Business card front">
    <div class="wordmark">
      <span class="wordmark__name">VELKOR</span>
      <span class="wordmark__sub">Services Inc.</span>
    </div>
    <div class="divider"></div>
    <div class="contact">
      <p class="contact__name">Marcus Hale</p>
      <p class="contact__title">Managing Director</p>
      <p class="contact__row">
        <svg viewBox="0 0 10 10"><path fill="var(--red)" d="M1 2c0-1 1-1.5 2-1.5l1 2-1 1c.5 1.2 1.3 2 2.5 2.5l1-1 2 1c0 1-.5 2-1.5 2C3.5 8 1 5.5 1 2z"/></svg>
        780-555-0142
      </p>
      <p class="contact__row">
        <svg viewBox="0 0 10 10"><rect x="0.5" y="2" width="9" height="6" fill="var(--red)"/><path d="M0.5 2l4.5 3.3L9.5 2" fill="none" stroke="#111" stroke-width=".9"/></svg>
        admin@velkor.ca
      </p>
      <p class="contact__row">
        <svg viewBox="0 0 10 10"><circle cx="5" cy="5" r="4.5" fill="var(--red)"/></svg>
        www.velkor.ca
      </p>
      <p class="contact__address">#305, 4820-27 Ave Northfield<br>Alberta, T2X 4K8 Canada</p>
    </div>
  </section>

  <section class="card card--back" aria-label="Business card back">
    <div class="wordmark">
      <span class="wordmark__name">VELKOR</span>
      <span class="wordmark__sub">Services Inc.</span>
    </div>
    <ul class="services" aria-label="Services">
      <li>Safety Compliance</li>
      <li>Fleet Audits</li>
      <li>Permits &amp; Licensing</li>
      <li>Driver Training</li>
      <li>IFTA &amp; IRP Filing</li>
      <li>Consulting</li>
    </ul>
  </section>
</body>
</html>
```